Washington DC Solo Practitioner Law Firm needs Stationery and Business Card Design

We need a letterhead and business card for a new law firm based in Washington DC called Harlow PLLC. The law firm is a single lawyer practicing appellate law (U.S. Supreme Court, Federal District Courts, State Supreme Courts).
We already have a logo designed through a MarkHive contest. The letterhead and the business card should include the Logo and have the same look and feel as the Logo - same fonts and colors, please. We would like a clean, crisp, simple, professional look. The design should convey stability and experience.
We have .png and .psd and .ai files for the logo, as needed
Dark blue color is PANTONE P 108-16 C
Grey color is PANTONE P 179-11 C
Type face is Century Gothic Regular typeface

```html
<!DOCTYPE html>
<html lang="en">
<head>
<meta charset="utf-8">
<title>Harlow PLLC Stationery</title>
<link href="https://fonts.googleapis.com/css2?family=Questrial&display=swap" rel="stylesheet">
<style>
:root{
  --navy:#1b4565;
  --grey:#9aa3ab;
  --paper:#ffffff;
  --backdrop:#eceef0;
  --ink:#5d6770;
}
*{margin:0;padding:0;box-sizing:border-box}
html,body{width:1200px;height:859px;overflow:hidden}
body{background:var(--backdrop);font-family:"Questrial",sans-serif;color:var(--navy);position:relative}
.sheet{position:absolute;background:var(--paper);box-shadow:0 2px 6px rgba(0,0,0,.12)}
.navy{background:var(--navy);color:#fff}

.lockup{display:flex;align-items:flex-start;gap:8px}
.lockup .mark{width:14px;height:14px;background:currentColor;flex:none;margin-top:2px}
.lockup .name{display:block;font-size:18px;letter-spacing:1px;line-height:1}
.lockup .suffix{display:block;font-size:8px;letter-spacing:6px;margin-top:3px;text-align:center}
.lockup .tagline{display:block;font-size:5.5px;letter-spacing:.6px;margin-top:3px;color:var(--grey)}
.navy .lockup .tagline{color:#c9d3dc}

.lockup--small{gap:6px}
.lockup--small .mark{width:10px;height:10px;margin-top:2px}
.lockup--small .name{font-size:14px;letter-spacing:.8px}
.lockup--small .suffix{font-size:6px;letter-spacing:4.5px;margin-top:2px}
.lockup--small .tagline{font-size:4.5px;letter-spacing:.4px;line-height:1.4;max-width:70px}

.letterhead{left:300px;top:40px;width:300px;height:410px}
.letterhead .lockup{position:absolute;left:28px;top:26px}
.letterhead .contact{position:absolute;right:22px;top:32px;font-size:5.5px;line-height:1.6;color:var(--ink);text-align:left}
.footer-band{position:absolute;left:0;bottom:26px;height:4px;background:var(--navy)}
.footer-band::after{content:"";position:absolute;right:-6px;top:-3px;width:9px;height:9px;background:var(--navy)}
.letterhead .footer-band{width:270px}

.card{width:180px;height:104px}
.card-back{left:40px;top:430px}
.card-back .lockup{position:absolute;left:46px;top:36px}
.card-front{left:40px;top:300px}
.card-front .lockup{position:absolute;left:12px;top:16px}
.card-front .person{position:absolute;left:110px;top:18px;font-size:5.5px;line-height:1.7;color:var(--ink)}
.card-front .person strong{display:block;color:var(--navy);font-weight:400;font-size:6.5px;letter-spacing:.5px}
.card-front .footer-band{width:160px;bottom:14px;height:3px}

.envelope{left:200px;top:500px;width:380px;height:180px}
.envelope .lockup{position:absolute;left:26px;top:24px}
.envelope .return{position:absolute;left:26px;top:90px;font-size:5.5px;color:var(--ink)}
.envelope .footer-band{width:350px;bottom:30px}

.folder{left:840px;top:90px;width:320px;height:450px}
.folder .lockup{position:absolute;left:120px;top:110px;transform:scale(1.3);transform-origin:left top}

.envelope-back{left:660px;top:600px;width:380px;height:180px}
.envelope-back .flap{position:absolute;left:0;top:0;width:100%;height:84px;background:var(--navy)}
.envelope-back .seal{position:absolute;left:184px;top:36px;width:12px;height:12px;background:#fff}
</style>
</head>
<body>

<section class="sheet letterhead" aria-label="Letterhead">
  <div class="lockup"><span class="mark"></span><div><span class="name">HARLOW</span><span class="suffix">PLLC</span><span class="tagline">TRIAL AND APPELLATE LITIGATION</span></div></div>
  <div class="contact">410 Meridian Row, Suite 200<br>Washington, DC 20004<br>T 202.555.0148<br>E office@harlowpllc.com</div>
  <div class="footer-band"></div>
</section>

<section class="sheet card card-front" aria-label="Business card front">
  <div class="lockup lockup--small"><span class="mark"></span><div><span class="name">HARLOW</span><span class="suffix">PLLC</span><span class="tagline">TRIAL AND APPELLATE LITIGATION</span></div></div>
  <div class="person"><strong>MORGAN ELLIS</strong>T 202.555.0148<br>F 202.555.0149<br>morgan@harlowpllc.com</div>
  <div class="footer-band"></div>
</section>

<section class="sheet card card-back navy" aria-label="Business card back">
  <div class="lockup"><span class="mark"></span><div><span class="name">HARLOW</span><span class="suffix">PLLC</span></div></div>
</section>

<section class="sheet envelope" aria-label="Envelope front">
  <div class="lockup"><span class="mark"></span><div><span class="name">HARLOW</span><span class="suffix">PLLC</span><span class="tagline">TRIAL AND APPELLATE LITIGATION</span></div></div>
  <div class="return">410 Meridian Row, Suite 200, Washington, DC 20004</div>
  <div class="footer-band"></div>
</section>

<section class="sheet folder navy" aria-label="Presentation folder">
  <div class="lockup"><span class="mark"></span><div><span class="name">HARLOW</span><span class="suffix">PLLC</span><span class="tagline">TRIAL AND APPELLATE LITIGATION</span></div></div>
</section>

<section class="sheet envelope-back" aria-label="Envelope back">
  <div class="flap"></div>
  <span class="seal"></span>
</section>

</body>
</html>
```